Pitch Deck and business cards for Virtual Reality Startup

We need a redesign of our pitch deck to be funky, creative and interactive with animated graphics inline with our product (VR training)
Note: the design does not have to be orange that's just a template of the information we're sending you so we would like to see other colours also.

Target Market(s)

Investors

Industry/Entity Type

Media

Contact Information for Business Card

logo, Name, title, address, telephone, email, website

Font styles to use
Other font styles liked:
• funky but readable

Colors

Designer to choose colors to be used in the design.

Requirements
Must have
• Exciting non traditional design that fits a new, innovative, exciting and interactive technology
Nice to have
• .
Should not have
• traditional look and feel.

```html
<!DOCTYPE html>
<html lang="en">
<head>
<meta charset="utf-8">
<title>Zephyr VR – Business Card</title>
<link rel="stylesheet" href="https://fonts.googleapis.com/css2?family=Montserrat:wght@600;700;800;900&family=Open+Sans:wght@400;600&display=swap">
<style>
  :root {
    --page-bg: #2a2a2c;
    --blue-light: #27a7e1;
    --blue-mid: #1488cf;
    --blue-deep: #0b63ad;
    --ink: #231f20;
    --paper: #f7f7f7;
    --paper-shade: #e9e9ea;
    --white: #ffffff;
    --muted: #dddddd;
  }
  * { box-sizing: border-box; margin: 0; padding: 0; }
  html, body {
    width: 1200px; height: 815px; overflow: hidden;
    background: var(--page-bg);
  }
  .sheet {
    position: relative; width: 1200px; height: 815px;
    display: flex; align-items: center; justify-content: center; gap: 40px;
  }
  .card {
    position: relative; width: 540px; height: 309px;
    border-radius: 22px; overflow: hidden;
    box-shadow: 0 14px 30px rgba(0,0,0,.45);
  }

  /* Front */
  .card--front {
    background: radial-gradient(ellipse at 35% 20%, var(--blue-light) 0%, var(--blue-mid) 45%, var(--blue-deep) 100%);
    display: flex; flex-direction: column; align-items: center; justify-content: center;
    color: var(--white);
  }
  .front__brand {
    font-family: "Montserrat", sans-serif; font-weight: 900;
    font-size: 64px; letter-spacing: 2px; line-height: 1;
  }
  .front__tagline {
    margin-top: 18px;
    font-family: "Montserrat", sans-serif; font-weight: 700;
    font-size: 14px; letter-spacing: 3px;
  }

  /* Back */
  .card--back { background: linear-gradient(180deg, var(--paper) 0%, var(--paper-shade) 100%); }
  .back__band, .back__photo {
    position: absolute; left: 0; top: 0; width: 540px; height: 309px;
  }
  .back__brand {
    position: absolute; left: 34px; top: 58px;
    font-family: "Montserrat", sans-serif; font-weight: 900;
    font-size: 30px; letter-spacing: 1px; line-height: 1.2; color: var(--ink);
  }
  .back__badge {
    position: absolute; left: 92px; top: 150px; width: 42px; height: 46px;
  }
  .back__claim {
    position: absolute; left: 48px; top: 203px; width: 130px;
    font-family: "Montserrat", sans-serif; font-weight: 800;
    font-size: 10px; line-height: 12px; text-align: center;
    color: var(--white); text-transform: uppercase;
  }
  .back__claim span { display: block; white-space: nowrap; }
  .contact {
    position: absolute; left: 330px; top: 82px; color: var(--white);
  }
  .contact__name {
    font-family: "Montserrat", sans-serif; font-weight: 800;
    font-size: 21px; letter-spacing: .5px; line-height: 1;
  }
  .contact__title {
    font-family: "Open Sans", sans-serif; font-weight: 400;
    font-size: 11px; line-height: 14px; color: var(--muted); margin-top: 4px;
  }
  .contact__list { list-style: none; margin-top: 11px; }
  .contact__item {
    display: flex; align-items: center; gap: 9px;
    font-family: "Open Sans", sans-serif; font-size: 10.5px; line-height: 14px;
    margin-bottom: 6px;
  }
  .contact__item svg { width: 12px; height: 12px; flex: none; }
  .back__address {
    position: absolute; left: 330px; top: 246px;
    font-family: "Open Sans", sans-serif; font-size: 11px;
    letter-spacing: 1px; color: var(--ink);
  }
</style>
</head>
<body>
<main class="sheet">

  <section class="card card--front" aria-label="Card front">
    <div class="front__brand">ZEPHYR VR</div>
    <div class="front__tagline">EXPERIENCE THE FUTURE OF TRAINING</div>
  </section>

  <section class="card card--back" aria-label="Card back">
    <svg class="back__band" viewBox="0 0 540 309" aria-hidden="true">
      <defs>
        <linearGradient id="blueBand" x1="0" y1="0" x2="1" y2="1">
          <stop offset="0" stop-color="#2a9fe0"/>
          <stop offset="1" stop-color="#0e6cb5"/>
        </linearGradient>
      </defs>
      <rect x="0" y="118" width="300" height="134" fill="url(#blueBand)"/>
      <rect x="260" y="70" width="280" height="130" fill="var(--ink)"/>
    </svg>

    <svg class="back__photo" viewBox="0 0 540 309" role="img" aria-label="Photo of a smiling woman wearing a VR headset, reaching out with one hand">
      <defs>
        <linearGradient id="photoTone" x1="0" y1="0" x2="1" y2="1">
          <stop offset="0" stop-color="#3aa6dd"/>
          <stop offset=".6" stop-color="#1b78bd"/>
          <stop offset="1" stop-color="#2a5d8a"/>
        </linearGradient>
      </defs>
      <polygon points="150,252 150,118 230,88 262,70 292,200 318,220 300,252" fill="url(#photoTone)"/>
    </svg>

    <div class="back__brand">ZEPHYR VR</div>

    <svg class="back__badge" viewBox="0 0 42 46" aria-hidden="true">
      <polygon points="21,0 42,11.5 42,34.5 21,46 0,34.5 0,11.5" fill="#164c7e"/>
    </svg>
    <p class="back__claim"><span>Benefit from</span><span>a job ready</span><span>workforce</span></p>

    <div class="contact">
      <div class="contact__name">YOUR NAME</div>
      <div class="contact__title">Company Director</div>
      <ul class="contact__list">
        <li class="contact__item">
          <svg viewBox="0 0 24 24" aria-hidden="true"><path fill="#fff" d="M6.6 10.8a15.1 15.1 0 0 0 6.6 6.6l2.2-2.2c.3-.3.7-.4 1-.2 1.1.4 2.3.6 3.6.6.6 0 1 .4 1 1V20c0 .6-.4 1-1 1A17 17 0 0 1 3 4c0-.6.4-1 1-1h3.5c.6 0 1 .4 1 1 0 1.3.2 2.5.6 3.6.1.3 0 .7-.2 1z"/></svg>
          1234 56 78 90
        </li>
        <li class="contact__item">
          <svg viewBox="0 0 24 24" aria-hidden="true"><path fill="#fff" d="M2 5h20v14H2zm2 2v.5l8 5 8-5V7z"/></svg>
          your@mail.com
        </li>
        <li class="contact__item">
          <svg viewBox="0 0 24 24" aria-hidden="true"><circle cx="12" cy="12" r="10" fill="none" stroke="#fff" stroke-width="2"/><path d="M2 12h20M12 2c3 3 3 17 0 20M12 2c-3 3-3 17 0 20" fill="none" stroke="#fff" stroke-width="1.6"/></svg>
          www.yourweb.com.
        </li>
      </ul>
    </div>

    <p class="back__address">Your official address is here</p>
  </section>

</main>
</body>
</html>
```